Water Filter Company Needs Bizz Cards!!

Need business cards for my company. We sell whole home water filters and salt free water softeners. No more buying bottled water. Our filtering units filter out all heavy metals, chlorine, and VOC's, last 15 years, and are maintenance free and supply your whole home with spring quality alkaline water. Our Salt free water conditioners, eliminate hard water and scale, without lowering the ph, or TDS's (total Dissolved solids)

I think this is the color code we are using on my site. My logo looks good behind it. #192841

Website will be www.Brevonix.com

Industry/Entity Type

Water Purification

Contact Information for Business Card

For now, just insert standard Dummy text. I need these text lines for the info to be editable so i can make them for multiple employees. I do have Photoshop and illustrator, unless there is a simpler program i can use solely for biz cards

Font styles to use
Sans Serif

Requirements
Must have
• Use my preexisting logo.

www.BrevoNix.com

Spring Quality Alkaline Water at every tap.

List out services. Whole Home Water Filters, Salt Free Water Softeners, Quendamar TX7, UV Sterilizers
Nice to have
• I think this is the color code we are using on my site. My logo looks good behind it. #192841 or black. Please no white or light blue backgrounds.

Maybe a picture of my tank.

Slogan like Spring Quality Alkaline Water at every tap.
And just list the services Whole Home Water Filters, Salt Free Water Softeners, Quendamar TX7, UV Sterilizers

I think I would like to not have a contrasting textured logo like I see on some of them. I may use it for my personal cards, but new employees may not want the extra expense.
Should not have
• A different logo than the one provided.

White or baby blue backgrounds. Use the color code, or blacks.

```html
<!DOCTYPE html>
<html lang="en">
<head>
<meta charset="utf-8">
<title>Brevonix Business Cards</title>
<link href="https://fonts.googleapis.com/css2?family=Montserrat:wght@700;800&family=Quicksand:wght@500;600&family=Teko:wght@500&display=swap" rel="stylesheet">
<style>
  :root{
    --navy:#192841;
    --black:#07090d;
    --sky:#2cb5ea;
    --stripe:#1a8fd6;
    --text:#e3e7ee;
    --muted:#c7cdd6;
    --stage:#4b4d50;
  }
  *{margin:0;padding:0;box-sizing:border-box}
  html,body{width:1200px;height:965px;overflow:hidden;background:var(--stage)}
  .card{position:absolute;left:230px;width:740px;height:423px;background:var(--navy);overflow:hidden}
  .card--front{top:40px}
  .card--back{top:500px}
  .tank{position:absolute;left:24px;top:40px;width:70px;height:350px;border-radius:14px 14px 22px 22px;
    background:linear-gradient(90deg,#0c0d10,#2a2c31 45%,#0c0d10)}
  .brand{position:absolute;display:flex;align-items:center;gap:14px;font-family:"Montserrat",sans-serif;font-weight:800;color:var(--sky);letter-spacing:-1px}
  .brand__dot{width:.62em;height:.62em;border-radius:50%;background:var(--sky)}
  .card--front .brand{left:190px;top:105px;font-size:74px}
  .card--back .brand{right:60px;top:40px;font-size:52px}
  .services{position:absolute;left:230px;top:235px;list-style:none;font-family:"Montserrat",sans-serif;font-weight:700;font-size:17px;letter-spacing:.5px;text-transform:uppercase;color:var(--text);line-height:26px}
  .services li{display:flex;align-items:center;gap:10px}
  .services li::before{content:"";width:8px;height:8px;border-radius:50%;background:var(--sky)}
  .back-art{position:absolute;inset:0}
  .person{position:absolute;left:70px;top:178px;font-family:"Quicksand",sans-serif}
  .person__name{font-family:"Montserrat",sans-serif;font-weight:800;font-size:34px;color:var(--sky);letter-spacing:.5px}
  .person__role{font-size:19px;color:var(--muted);font-weight:500;margin-top:-2px}
  .contacts{position:absolute;left:70px;top:252px;list-style:none;font-family:"Quicksand",sans-serif;font-weight:500;font-size:18px;color:var(--muted);line-height:25px}
  .contacts li,.address{display:flex;align-items:center;gap:12px}
  .icon{width:16px;height:16px;flex:none}
  .address{position:absolute;left:70px;top:360px;font-family:"Quicksand",sans-serif;font-weight:500;font-size:19px;color:var(--text);line-height:23px}
  .slogan{position:absolute;right:22px;top:246px;font-family:"Teko",sans-serif;font-weight:500;font-size:25px;color:var(--sky);text-transform:uppercase;letter-spacing:.3px}
</style>
</head>
<body>
  <section class="card card--front">
    <div class="tank" role="img" aria-label="Photo of the whole home filter tank"></div>
    <div class="brand"><span class="brand__dot"></span>Brevonix</div>
    <ul class="services">
      <li>Whole Home Water Filters</li>
      <li>Salt Free Water Softeners</li>
      <li>Quendamar TX7</li>
      <li>UV Sterilizers</li>
    </ul>
  </section>

  <section class="card card--back">
    <svg class="back-art" width="740" height="423" viewBox="0 0 740 423" aria-hidden="true">
      <path d="M0,348 L330,348 C372,348 378,290 430,290 L740,290 L740,423 L0,423 Z" fill="var(--black)"/>
      <path d="M505,277 L740,277 L740,291 L520,291 Z" fill="var(--stripe)"/>
    </svg>
    <div class="brand"><span class="brand__dot"></span>Brevonix</div>
    <div class="slogan">Spring quality alkaline water at every tap</div>
    <div class="person">
      <div class="person__name">JOHN SMITH</div>
      <div class="person__role">CEO/ Owner</div>
    </div>
    <ul class="contacts">
      <li><svg class="icon" viewBox="0 0 16 16"><path d="M4 1.5l2.2 3-1.4 1.6a9 9 0 0 0 5 5l1.6-1.4 3 2.2-1.3 2.4C8 14 2 8 1.6 2.8Z" fill="none" stroke="var(--sky)" stroke-width="1.4"/></svg>( 84) 0123 456 789</li>
      <li><svg class="icon" viewBox="0 0 16 16"><rect x="1" y="3" width="14" height="10" fill="none" stroke="var(--sky)" stroke-width="1.4"/><path d="M1 3l7 6 7-6" fill="none" stroke="var(--sky)" stroke-width="1.4"/></svg>contact@company.com</li>
      <li><svg class="icon" viewBox="0 0 16 16"><circle cx="8" cy="8" r="7" fill="var(--sky)"/><path d="M1 8h14M8 1c-3 3-3 11 0 14M8 1c3 3 3 11 0 14" fill="none" stroke="var(--navy)" stroke-width="1.1"/></svg>www.BrevoNix.com</li>
    </ul>
    <div class="address">
      <svg class="icon" viewBox="0 0 16 16" style="width:20px;height:22px"><path d="M8 15s5-5 5-9A5 5 0 0 0 3 6c0 4 5 9 5 9Z" fill="none" stroke="var(--sky)" stroke-width="1.4"/><circle cx="8" cy="6" r="1.8" fill="none" stroke="var(--sky)" stroke-width="1.4"/></svg>
      <div>11100956 Linden Street<br>Washington DC, USA</div>
    </div>
  </section>
</body>
</html>
```